Regional Consulting Business Needs a Business Card Design

We need a business card design for our new business based in Regional Victoria, Australia called Brindle Power. We are a consulting company with our main goal being to save people momey money and reducing their carbon footprint. Anything from water saving showerheads, to energy saving lightglobes and even to solar power. We would like to see designs that use bright colours. The final design should shout 'we are here to help you'.

Industry/Entity Type

Business

```html
<!DOCTYPE html>
<html lang="en">
<head>
<meta charset="utf-8">
<title>Brindle Power – Business Card</title>
<link rel="stylesheet" href="https://fonts.googleapis.com/css2?family=Tinos:ital,wght@0,400;0,700;1,700&family=Questrial&display=swap">
<style>
  :root {
    --stage: #ecebe8;
    --card: #ffffff;
    --ink-dark: #3a3a3a;
    --ink-mid: #555555;
    --ink-soft: #4a4a4a;
    --band: #4a4847;
    --accent: #f0a830;
    --rule: #3a3a3a;
  }
  * { margin: 0; padding: 0; box-sizing: border-box; }
  html, body { width: 1200px; height: 407px; overflow: hidden; }
  body { background: var(--stage); position: relative; }

  .card {
    position: absolute;
    background: var(--card);
    border-radius: 28px;
    overflow: hidden;
    box-shadow: 0 2px 6px rgba(0,0,0,0.18);
  }
  .card--front { left: 62px; top: 50px; width: 526px; height: 302px; }
  .card--back  { left: 618px; top: 46px; width: 525px; height: 300px; }

  /* Front */
  .brand { position: absolute; left: 72px; top: 28px; }
  .brand__mark {
    position: absolute; left: 0; top: 6px;
    width: 52px; height: 52px;
    background: var(--accent);
  }
  .brand__name {
    position: absolute; left: 66px; top: 8px; white-space: nowrap;
    font-family: "Tinos", serif; font-weight: 700;
    font-size: 40px; line-height: 1; color: var(--ink-dark);
  }
  .brand__tagline {
    position: absolute; left: 52px; top: 64px; white-space: nowrap;
    font-family: "Tinos", serif; font-weight: 700; font-style: italic;
    font-size: 15px; color: var(--ink-dark);
  }

  .person { position: absolute; right: 295px; top: 158px; text-align: right; font-family: "Tinos", serif; }
  .person__name { font-size: 25px; font-weight: 700; color: var(--ink-mid); line-height: 1.2; }
  .person__title { font-size: 16px; color: var(--ink-mid); margin-top: 2px; }

  .divider { position: absolute; left: 253px; top: 140px; width: 1px; height: 86px; background: var(--rule); }

  .contact { position: absolute; left: 265px; top: 139px; list-style: none; font-family: "Tinos", serif; font-size: 17px; color: var(--ink-dark); }
  .contact li { display: flex; align-items: center; height: 23px; }
  .contact svg { width: 12px; height: 12px; margin-right: 5px; fill: var(--ink-dark); }

  .footer-band { position: absolute; left: 0; top: 0; width: 526px; height: 302px; }
  .address {
    position: absolute; left: 0; right: 0; top: 268px; text-align: center;
    font-family: "Tinos", serif; font-size: 17px; color: #ffffff;
  }

  /* Back */
  .package { position: absolute; inset: 0; text-align: center; font-family: "Questrial", sans-serif; color: var(--ink-soft); }
  .package__title { position: absolute; left: 0; right: 0; top: 40px; font-size: 18px; font-weight: 700; color: var(--ink-dark); letter-spacing: 0.3px; }
  .package__list { list-style: none; position: absolute; left: 0; right: 0; top: 86px; font-size: 14.5px; line-height: 17px; }
  .package__list li { margin-bottom: 18px; }
  .package__list li::before { content: "\2022\00a0"; }
</style>
</head>
<body>
  <section class="card card--front">
    <svg class="footer-band" viewBox="0 0 526 302" aria-hidden="true">
      <path d="M0 282 Q263 218 526 282" fill="none" stroke="var(--accent)" stroke-width="3"/>
      <path d="M0 290 Q263 232 526 290 L526 302 L0 302 Z" fill="var(--band)"/>
    </svg>

    <div class="brand">
      <div class="brand__mark"></div>
      <div class="brand__name">Brindle Power</div>
      <div class="brand__tagline">Maintanence and consulting services</div>
    </div>

    <div class="person">
      <div class="person__name">Your Name</div>
      <div class="person__title">Title</div>
    </div>

    <div class="divider"></div>

    <ul class="contact">
      <li><svg viewBox="0 0 12 12"><path d="M2 1h3l1 3-2 1a7 7 0 0 0 3 3l1-2 3 1v3c-6 0-10-4-10-9z"/></svg>123-456-7890</li>
      <li><svg viewBox="0 0 12 12"><rect x="3" y="1" width="6" height="3"/><rect x="1" y="4" width="10" height="5" rx="1"/><rect x="3" y="8" width="6" height="3"/></svg>123-456-7890</li>
      <li><svg viewBox="0 0 12 12"><path d="M1 3h10v6H1z M1 3l5 4 5-4" fill="none" stroke="var(--ink-dark)" stroke-width="1.4"/></svg>123abcd@brindlemail.com</li>
      <li><svg viewBox="0 0 12 12"><circle cx="6" cy="6" r="5" fill="none" stroke="var(--ink-dark)" stroke-width="1.2"/><path d="M1 6h10M6 1v10" stroke="var(--ink-dark)" stroke-width="1"/></svg>www.123abcd.com</li>
    </ul>

    <div class="address">Street Name, City, State, zip code</div>
  </section>

  <section class="card card--back">
    <div class="package">
      <h2 class="package__title">Product Package</h2>
      <ul class="package__list">
        <li>Free energy assessment of your home or business</li>
        <li>Free advice on energy and water sustainability</li>
        <li>Free gas and solar hot water rebate eligibility assessment</li>
        <li>Free solar power rebate eligibility assessment</li>
        <li>We offer rebates of up to $2000 for the purchase and<br>implementation of a range of eligible water reduction and<br>sustainability products, appliances and services.</li>
      </ul>
    </div>
  </section>
</body>
</html>
```